Business cards for Marrowfield Consulting with the following info for the front side:

Marrowfield Consulting
Executive Coaching and Human Capital Strategy
www.marrowfield.example

Idalia Renvoort
Principal
idalia@marrowfield.example
+1 555 274 9186

Black background, text using the colours of the logo - enclosed.

The back side of the business card should feature the logo in the middle, with "Executive Coaching and Human Capital Strategy" on top and "www.marrowfield.example" below.

```html
<!DOCTYPE html>
<html lang="en">
<head>
<meta charset="utf-8">
<title>Marrowfield Consulting – Business Cards</title>
<link href="https://fonts.googleapis.com/css2?family=Lato:wght@400;700;900&display=swap" rel="stylesheet">
<style>
  :root {
    --backdrop: #3a332f;
    --card: #0b0b0b;
    --blue: #2ba8e2;
    --yellow: #f6c21c;
    --gold-line: #8a7436;
    --text: #d9d9d9;
    --muted: #bdbdbd;
  }
  * { box-sizing: border-box; margin: 0; padding: 0; }
  html, body { width: 1200px; height: 847px; overflow: hidden; }
  body {
    background: var(--backdrop);
    font-family: "Lato", sans-serif;
    position: relative;
  }
  .card {
    position: absolute;
    width: 520px;
    height: 297px;
    background: var(--card);
    box-shadow: 2px 3px 0 var(--yellow), 0 18px 40px rgba(0,0,0,.45);
  }
  .card--back { left: 50px; top: 275px; }
  .card--front { left: 630px; top: 275px; }

  /* brand lockup */
  .brand { display: flex; align-items: center; gap: 12px; }
  .brand__mark {
    width: 44px; height: 44px; border-radius: 50%;
    border: 3px solid var(--blue); flex: none;
  }
  .brand__name {
    color: var(--blue); font-weight: 700; letter-spacing: 1px;
    font-size: 40px; line-height: 1;
  }

  /* back side */
  .card--back .brand { position: absolute; left: 62px; top: 88px; }
  .back__tagline {
    position: absolute; left: 118px; top: 146px;
    color: var(--text); font-size: 15px; font-style: normal;
  }
  .back__url {
    position: absolute; left: 0; right: 0; top: 218px; text-align: center;
    color: var(--text); font-size: 15px; letter-spacing: 3px;
  }
  .back__url .accent { color: var(--yellow); }

  /* front side */
  .card--front .brand { position: absolute; left: 30px; top: 124px; gap: 8px; }
  .card--front .brand__mark { width: 30px; height: 30px; border-width: 2px; }
  .card--front .brand__name { font-size: 24px; }
  .front__divider {
    position: absolute; left: 262px; top: 58px; width: 1px; height: 182px;
    background: var(--gold-line);
  }
  .details { position: absolute; left: 286px; top: 52px; right: 20px; }
  .details__name { color: var(--blue); font-weight: 900; font-size: 26px; line-height: 1.1; }
  .details__role { color: var(--muted); font-size: 15px; margin-bottom: 8px; }
  .details__company { color: var(--yellow); font-weight: 700; font-size: 15px; }
  .details__tagline { color: var(--text); font-size: 15px; line-height: 1.25; margin-bottom: 8px; }
  .contact { list-style: none; }
  .contact li {
    display: flex; align-items: center; gap: 8px;
    color: var(--text); font-size: 15px; line-height: 1.45;
  }
  .contact svg { width: 14px; height: 14px; flex: none; }
</style>
</head>
<body>

<section class="card card--back" aria-label="Card back">
  <div class="brand">
    <span class="brand__mark"></span>
    <span class="brand__name">MARROWFIELD</span>
  </div>
  <p class="back__tagline">Executive Coaching and Human Capital Strategy</p>
  <p class="back__url">www.<span class="accent">marrowfield</span>.example</p>
</section>

<section class="card card--front" aria-label="Card front">
  <div class="brand">
    <span class="brand__mark"></span>
    <span class="brand__name">MARROWFIELD</span>
  </div>
  <div class="front__divider"></div>
  <div class="details">
    <h1 class="details__name">Idalia Renvoort</h1>
    <p class="details__role">Principal</p>
    <p class="details__company">Marrowfield Consulting</p>
    <p class="details__tagline">Executive Coaching and Human Capital Strategy</p>
    <ul class="contact">
      <li>
        <svg viewBox="0 0 24 24" fill="var(--yellow)" aria-hidden="true"><path d="M6.6 10.8a15 15 0 0 0 6.6 6.6l2.2-2.2a1 1 0 0 1 1-.25 11.4 11.4 0 0 0 3.6.57 1 1 0 0 1 1 1V20a1 1 0 0 1-1 1A17 17 0 0 1 3 4a1 1 0 0 1 1-1h3.5a1 1 0 0 1 1 1c0 1.25.2 2.45.57 3.57a1 1 0 0 1-.25 1z"/></svg>
        +1 555 274 9186
      </li>
      <li>
        <svg viewBox="0 0 24 24" fill="none" stroke="var(--yellow)" stroke-width="2" aria-hidden="true"><rect x="2" y="5" width="20" height="14"/><path d="M2 5l10 8 10-8"/></svg>
        idalia@marrowfield.example
      </li>
      <li>
        <svg viewBox="0 0 24 24" fill="none" stroke="var(--yellow)" stroke-width="2" aria-hidden="true"><circle cx="12" cy="12" r="10"/><path d="M2 12h20M12 2c3 3 3 17 0 20M12 2c-3 3-3 17 0 20"/></svg>
        www.marrowfield.example
      </li>
    </ul>
  </div>
</section>

</body>
</html>
```